Lanterns Over The Quiet Meadow Waters Book Cover

Book cover for a new book titled "Lanterns Over The Quiet Meadow Waters" which will show how retirees can pay NO tax in their retirement. Would like you to use your creative inspiration to come up with a design.

Please make MEADOW WATERS the emphasis of the title.

can you show money being rescued, or freed, from taxes.

I'm trying convey the message that retirees can FREE themselves from the burden of taxes in retirement by reading this book and following the instructions. Think about a person swimming with a weight on his back, sinking him. Suddenly the weight is removed. The feeling and imagery of the load being light now

Doing MEADOW WATERS can alleviate many of unnecessary taxes which will weight retirees down. But, unfortunately, many advisors in my industry do not educate their clients on this stuff.

Not a fan of dark backgrounds, generally speaking. Lighter is good.

Remember folks, go to brindlecart. Type in Roth IRA books. what will jump out over the stuff that's already there? Thanks!

Target Market(s)

recent, or soon to be, retirees, people in their 50s and 60s, typically couples

Industry/Entity Type

Financial

Font styles to use
Serif

Colors

Designer to choose colors to be used in the design.

Requirements
Must have
• Be optimistic, sunny, happy. How you do that? I don't know, that's why I'm hiring you. This book is designed for the lay person, (average Joe and Jane)
• Put my picture on the lower back.
• My name at bottom of the cover
Nice to have
• Be nice to have the cover POP on Brindlecart because I'm competing with so many other books and thumbnails
• Maybe a kite with a dollar bill that is breaking from a ball and chain? Just an idea.
Should not have
• No guys in suits. Happy couples sitting on the beach or sailing. That stuff is in every piece of financial planning literature.
• NOT TECHNICAL. NO PIGGY BANKS Design please

```html
<!DOCTYPE html>
<html lang="en">
<head>
<meta charset="UTF-8">
<title>Lanterns Over The Quiet Meadow Waters — Cover Spread</title>
<link rel="stylesheet" href="https://fonts.googleapis.com/css2?family=Cormorant+Garamond:ital,wght@0,500;0,600;1,500;1,600&family=Cinzel:wght@500;600&family=Lora:wght@400&display=swap">
<style>
  :root {
    --page-bg: #eceeea;
    --paper: #ffffff;
    --title-dark: #2d3a2a;
    --title-green: #3f8b34;
    --body-ink: #3a3a3a;
    --grass-light: #8cc63f;
    --grass-dark: #4f8f22;
    --door-light: #dfe9f3;
    --door-dark: #9fb6cc;
    --money-light: #cfe0c0;
    --money-dark: #7f9f6c;
    --photo-light: #c9cfd6;
    --photo-dark: #8a939e;
    --spine-edge: #d9ddd6;
  }
  html, body {
    margin: 0;
    padding: 0;
    overflow: hidden;
  }
  body {
    width: 900px;
    height: 1200px;
    background: var(--page-bg);
    position: relative;
  }
  .cover-spread {
    position: absolute;
    left: 10px;
    top: 365px;
    width: 880px;
    height: 470px;
    display: flex;
    background: var(--paper);
    box-shadow: 0 2px 10px rgba(0,0,0,0.12);
  }
  .back-cover, .front-cover {
    position: relative;
    width: 420px;
    height: 100%;
    overflow: hidden;
  }
  .spine {
    position: relative;
    width: 40px;
    height: 100%;
    border-left: 1px solid var(--spine-edge);
    border-right: 1px solid var(--spine-edge);
    box-sizing: border-box;
  }
  .grass-band {
    position: absolute;
    left: 0;
    right: 0;
    bottom: 0;
    height: 46px;
    background: linear-gradient(180deg, var(--grass-light), var(--grass-dark));
  }
  .back-blurb {
    position: absolute;
    left: 30px;
    top: 34px;
    width: 360px;
    font-family: "Lora", serif;
    font-size: 11.5px;
    line-height: 1.55;
    color: var(--body-ink);
  }
  .back-blurb p { margin: 0 0 12px; }
  .author-bio {
    position: absolute;
    left: 30px;
    top: 250px;
    width: 360px;
    display: flex;
    gap: 16px;
    align-items: flex-start;
  }
  .author-photo {
    flex: 0 0 110px;
    height: 120px;
    background: linear-gradient(160deg, var(--photo-light), var(--photo-dark));
  }
  .author-bio p {
    margin: 0;
    font-family: "Lora", serif;
    font-size: 10.5px;
    line-height: 1.5;
    color: var(--body-ink);
  }
  .spine-author {
    position: absolute;
    left: 50%;
    bottom: 60px;
    transform: translateX(-50%) rotate(90deg);
    transform-origin: center;
    font-family: "Cinzel", serif;
    font-size: 9px;
    letter-spacing: 1.5px;
    color: var(--title-green);
    white-space: nowrap;
  }
  .spine-title {
    position: absolute;
    left: 50%;
    top: 150px;
    transform: translateX(-50%) rotate(90deg);
    font-family: "Cormorant Garamond", serif;
    font-size: 11px;
    font-weight: 600;
    color: var(--title-dark);
    white-space: nowrap;
  }
  .front-title {
    position: absolute;
    left: 20px;
    top: 26px;
    width: 380px;
    text-align: center;
    margin: 0;
    font-weight: 600;
  }
  .title-lead {
    display: block;
    font-family: "Cormorant Garamond", serif;
    font-style: italic;
    font-size: 24px;
    color: var(--title-dark);
    line-height: 1.1;
  }
  .title-middle {
    display: block;
    font-family: "Cinzel", serif;
    font-size: 26px;
    color: var(--title-green);
    letter-spacing: 1px;
    line-height: 1.25;
  }
  .title-emphasis {
    display: block;
    font-family: "Cormorant Garamond", serif;
    font-style: italic;
    font-size: 38px;
    color: var(--title-dark);
    line-height: 1.05;
  }
  .front-scene {
    position: absolute;
    left: 0;
    top: 170px;
    width: 420px;
    height: 254px;
  }
  .door-with-money {
    position: absolute;
    left: 150px;
    top: 20px;
    width: 200px;
    height: 240px;
    background: linear-gradient(90deg, var(--money-dark) 0%, var(--money-light) 45%, var(--door-light) 62%, var(--door-dark) 100%);
    border-radius: 4px 4px 0 0;
  }
  .front-author {
    position: absolute;
    left: 0;
    right: 0;
    bottom: 12px;
    text-align: center;
    font-family: "Cinzel", serif;
    font-size: 17px;
    font-weight: 600;
    letter-spacing: 3px;
    color: var(--title-green);
    z-index: 2;
  }
  .front-cover .grass-band { height: 56px; }
</style>
</head>
<body>
  <section class="cover-spread">
    <div class="back-cover">
      <div class="back-blurb">
        <p>Most retirees pay far more tax than they need to, simply because no one showed them another way. This book walks through each step in plain language, so you can keep more of what you saved and enjoy the years ahead with less worry.</p>
        <p>Inside you will find simple examples, clear checklists and honest answers to the questions people ask most. No jargon, no charts to decode, just a friendly guide to lightening the load you carry into retirement.</p>
      </div>
      <div class="author-bio">
        <div class="author-photo" role="img" aria-label="Portrait photo of the author"></div>
        <p>Dale Whitford has spent two decades helping families plan for life after work. He writes for everyday readers and believes good advice should be easy to follow. He lives by the lake with his wife and two dogs.</p>
      </div>
      <div class="grass-band" role="img" aria-label="Green grass along the bottom edge"></div>
    </div>

    <div class="spine">
      <span class="spine-title">Lanterns Over The Quiet Meadow Waters</span>
      <span class="spine-author">DALE WHITFORD</span>
    </div>

    <div class="front-cover">
      <h1 class="front-title">
        <span class="title-lead">Lanterns Over</span>
        <span class="title-middle">The Quiet</span>
        <span class="title-emphasis">Meadow Waters</span>
      </h1>
      <div class="front-scene">
        <div class="door-with-money" role="img" aria-label="Illustration of an open blue door with a fan of dollar bills bursting out, standing on grass"></div>
      </div>
      <div class="grass-band" role="img" aria-label="Green grass meadow along the bottom edge"></div>
      <div class="front-author">DALE WHITFORD</div>
    </div>
  </section>
</body>
</html>
```